Wordpress website update with basic ecomm features

We need an update to our existing website
www.quillharbour.com.au that can be easily updated, enhances our logo and can take payments online and a basic text logo suite for 3 products. Website would reflect confidence and give clients confidence in the outcomes we will provide for them. must be easy to use, crisp, fresh, clean and dynamic.

Target Market(s)

entrepreneurs, professionals, small business owners, corporate organisations, universities

Industry/Entity Type

Online

Coding

Coded - Design and coding required

Number of Pages Required

5+ page

Font styles to use
Sans Serif

Requirements
Must have
• be easy to navigate, look professional, please see brief doc
Nice to have
• please see briefing doc
Should not have
• please see briefing doc

```html
<!DOCTYPE html>
<html lang="en">
<head>
<meta charset="utf-8">
<title>Quill Harbour — Australian Business Entrepreneurship</title>
<link href="https://fonts.googleapis.com/css2?family=Open+Sans:wght@400;600;700&display=swap" rel="stylesheet">
<style>
  :root {
    --header-bg: #ffffff;
    --ink: #111111;
    --hero-dark: #383836;
    --hero-mid: #4a4a47;
    --headline: #8d8d8d;
    --cta: #0c71c3;
    --cta-text: #ffffff;
  }
  * { margin: 0; padding: 0; box-sizing: border-box; }
  html, body {
    width: 1200px; height: 1200px; overflow: hidden;
    font-family: "Open Sans", Arial, sans-serif;
    background: var(--header-bg);
  }
  .page { position: relative; width: 1200px; height: 1200px; }

  .site-header { position: absolute; top: 0; left: 0; width: 1200px; height: 250px; background: var(--header-bg); }
  .nav-link {
    position: absolute; top: 105px;
    font-size: 23px; font-weight: 700; color: var(--ink);
    text-decoration: none; white-space: nowrap;
  }
  .brand { position: absolute; left: 460px; top: 33px; width: 230px; text-align: center; }
  .brand-square { width: 162px; height: 161px; margin: 0 auto; background: var(--ink); border-radius: 8px; }
  .brand-name {
    margin-top: 13px; font-size: 17px; font-weight: 400;
    letter-spacing: 7px; margin-right: -7px; color: var(--ink); white-space: nowrap;
  }
  .search-icon { position: absolute; left: 1155px; top: 112px; }

  .hero { position: absolute; top: 250px; left: 0; width: 1200px; height: 950px; overflow: hidden; }
  .hero-photo {
    position: absolute; inset: 0;
    background: linear-gradient(180deg, var(--hero-dark) 0%, var(--hero-mid) 45%, var(--hero-dark) 100%);
  }
  .hero-title {
    position: absolute; left: 0; top: 194px; width: 1264px;
    text-align: center; color: var(--headline);
    font-size: 122px; font-weight: 700; line-height: 116px; letter-spacing: -3px;
  }
  .cta {
    position: absolute; left: 516px; top: 610px; width: 230px; height: 62px;
    background: var(--cta); border: 2px solid #ffffff; border-radius: 3px;
    color: var(--cta-text); font-size: 25px; font-weight: 700;
    display: flex; align-items: center; justify-content: center; text-decoration: none;
  }
</style>
</head>
<body>
<div class="page">
  <header class="site-header">
    <a class="nav-link" style="left:81px">Home</a>
    <a class="nav-link" style="left:186px">About Us</a>
    <a class="nav-link" style="left:328px">Events</a>
    <div class="brand">
      <div class="brand-square"></div>
      <div class="brand-name">QUILL HARBOUR</div>
    </div>
    <a class="nav-link" style="left:741px">Media</a>
    <a class="nav-link" style="left:846px">Testimonials</a>
    <a class="nav-link" style="left:1030px">Contact</a>
    <svg class="search-icon" width="24" height="26" viewBox="0 0 24 26" aria-label="Search">
      <circle cx="14" cy="10" r="8" fill="none" stroke="#111" stroke-width="2"/>
      <line x1="8.5" y1="16" x2="2" y2="23" stroke="#111" stroke-width="2.2" stroke-linecap="round"/>
    </svg>
  </header>

  <section class="hero">
    <div class="hero-photo" role="img" aria-label="Blurred, darkened photo of professionals meeting in an office"></div>
    <h1 class="hero-title">Australian<br>Business<br>Entrepreneurship</h1>
    <a class="cta">LETS LAUNCH</a>
  </section>
</div>
</body>
</html>
```